Desk Allies Business Card

Contact Information for Business Card

Janne Voutilainen
Managing Director

3/47 Brindle Street Larchfield ACT 2914

Tel: +61 02 6257 3140
Mob: +61 0427 315 846

Email: janne@deskallies.com.au
Web: www.deskallies.com.au

Colors

Designer to choose colors to be used in the design.

Requirements
Must have
• Logo, Name, Title, Address, Telephone, Mobile, Email Address and Website
• "Desk Ally International Pty Ltd"

```html
<!DOCTYPE html>
<html lang="en">
<head>
<meta charset="utf-8">
<title>Desk Allies Business Card</title>
<link href="https://fonts.googleapis.com/css2?family=Arimo:wght@400;700&family=Source+Sans+3:wght@400;600&display=swap" rel="stylesheet">
<style>
  :root {
    --page: #ffffff;
    --page-edge: #e4e4e4;
    --brand-blue: #2b84f5;
    --brand-cyan: #00ffff;
    --ink: #1a1a1a;
    --black: #000000;
    --white: #ffffff;
    --front-centre: #ffffff;
    --front-edge: #dbe4e6;
  }
  * { margin: 0; padding: 0; box-sizing: border-box; }
  html, body { width: 908px; height: 1200px; overflow: hidden; background: var(--page); }
  .sheet {
    position: relative;
    width: 908px; height: 1200px;
    border: 1px solid var(--page-edge);
    background: var(--page);
  }
  .card { position: absolute; width: 574px; height: 328px; overflow: hidden; }

  /* Front */
  .card-front {
    left: 175px; top: 211px;
    background: radial-gradient(ellipse at 55% 50%, var(--front-centre) 20%, var(--front-edge) 100%);
    font-family: "Arimo", Arial, sans-serif;
  }
  .brand {
    position: absolute; left: 22px; top: 145px;
    display: flex; align-items: center; gap: 9px;
  }
  .brand-dot {
    width: 35px; height: 35px; border-radius: 50%;
    background: var(--brand-blue);
  }
  .brand-name {
    font-family: "Arimo", Arial, sans-serif;
    font-weight: 700; font-size: 17px;
    color: var(--brand-blue); letter-spacing: 0.2px;
    text-transform: uppercase;
  }
  .divider {
    position: absolute; left: 242px; top: 86px;
    width: 1.5px; height: 155px; background: var(--ink);
  }
  .person-name {
    position: absolute; left: 263px; top: 100px;
    font-size: 22px; font-weight: 400; color: var(--brand-blue); letter-spacing: 0.3px;
    text-transform: uppercase; white-space: nowrap;
  }
  .person-title {
    position: absolute; left: 295px; top: 132px;
    font-size: 12.5px; color: var(--ink); letter-spacing: 0.2px;
  }
  .contact {
    position: absolute; left: 263px;
    display: flex; align-items: center;
    font-family: "Source Sans 3", sans-serif; font-size: 15px; color: var(--ink);
  }
  .contact svg { width: 16px; height: 20px; margin-right: 15px; }
  .contact-phone { top: 164px; }
  .contact-email { top: 192px; }

  /* Back */
  .card-back {
    left: 176px; top: 586px;
    background: var(--white);
    border: 1px solid var(--page-edge);
    font-family: "Source Sans 3", sans-serif;
  }
  .back-field {
    position: absolute; top: 0; bottom: 0; left: 190px; right: 0;
    background: linear-gradient(90deg, var(--brand-blue) 0%, var(--black) 30%);
  }
  .back-brand {
    position: absolute; left: 36px; top: 150px;
    display: flex; align-items: center; gap: 8px;
  }
  .back-brand .brand-dot { width: 26px; height: 26px; }
  .back-brand .brand-name { font-size: 17px; }
  .company-details {
    position: absolute; right: 31px; top: 164px;
    text-align: right; color: var(--white);
    font-size: 19px; line-height: 22px; white-space: nowrap;
  }
  .company-name { margin-bottom: 18px; }
</style>
</head>
<body>
<main class="sheet">

  <section class="card card-front">
    <div class="brand">
      <span class="brand-dot"></span>
      <span class="brand-name">Desk Allies</span>
    </div>
    <div class="divider"></div>
    <h1 class="person-name">Janne Voutilainen</h1>
    <p class="person-title">MANAGING DIRECTOR</p>
    <p class="contact contact-phone">
      <svg viewBox="0 0 16 20" aria-hidden="true"><rect x="2" y="1" width="12" height="18" rx="1.5" fill="none" stroke="#333" stroke-width="1"/><line x1="6.5" y1="16.5" x2="9.5" y2="16.5" stroke="#333" stroke-width="1"/></svg>
      +61 0427 315 846
    </p>
    <p class="contact contact-email">
      <svg viewBox="0 0 16 20" aria-hidden="true"><text x="8" y="15" text-anchor="middle" font-family="Arial, sans-serif" font-size="16" fill="#333">@</text></svg>
      janne@deskallies.com.au
    </p>
  </section>

  <section class="card card-back">
    <div class="back-field" role="img" aria-label="Decorative curved wave area in cyan, blue and black"></div>
    <div class="back-brand">
      <span class="brand-dot"></span>
      <span class="brand-name">Desk Allies</span>
    </div>
    <div class="company-details">
      <p class="company-name">Desk Ally International Pty Ltd</p>
      <p>3/47 Brindle Street Larchfield ACT 2914</p>
      <p>Tel: +61 02 6257 3140</p>
      <p>www.deskallies.com.au</p>
    </div>
  </section>

</main>
</body>
</html>
```